I have an account on Plumetry through Tanvrik, so the design will need to be built there. I already have a logo, and the design of the website should at least compliment the look of the logo. The placeholder website where the logo can be seen is at www.velmarconsulting.example. The purpose of the website at this point in time is not to drive business, but rather, to have a strong appearance and add some credibility to my already existing business.

The website should have some level of abstraction about it. I prefefer designs and shapes of images of people. The fewer people, the better. No stock photography of people standing around talking to each other.

Number of Pages Required

4 page

Requirements
Must have
• The ability to work on my existing Plume Try Account
Should not have
• Stock photography of people standing around doing "business-y" stuff. That is sooo old and played out, and is the opposite of the type of message I am trying to portray.

```html
<!DOCTYPE html>
<html lang="en">
<head>
<meta charset="utf-8">
<title>Velmar Consulting</title>
<link href="https://fonts.googleapis.com/css2?family=Mulish:wght@400;600;700;800&family=Lora:wght@400&display=swap" rel="stylesheet">
<style>
  :root{
    --orange:#f07f2a;
    --ink:#55585b;
    --muted:#8d9094;
    --line:#cfd1d3;
    --gap:#ececec;
    --white:#ffffff;
  }
  *{box-sizing:border-box;margin:0;padding:0}
  html,body{width:682px;height:1200px;overflow:hidden;background:var(--gap)}
  body{position:relative;font-family:"Mulish",sans-serif;color:var(--ink)}
  .page{position:absolute;left:0;width:682px;background:var(--white)}
  .page--home{top:0;height:375px}
  .page--services{top:420px;height:364px}
  .page--contact{top:818px;height:382px}
  .abs{position:absolute}
  .brand{left:32px;top:12px;display:flex;align-items:center;gap:5px;font-size:9px;font-weight:800;color:var(--ink);letter-spacing:.5px}
  .brand-mark{width:9px;height:9px;background:var(--orange)}
  .nav{right:40px;top:13px;display:flex;gap:16px;font-size:6px;font-weight:700;letter-spacing:.6px;color:var(--muted)}
  .nav .is-current{color:#b9bbbe}
  .nav-rule{left:0;right:0;top:30px;height:1px;background:#eeeeee}
  .accent-bar{width:4px;background:var(--orange)}
  .hero-title{left:46px;top:163px;font-size:31px;font-weight:800;letter-spacing:.6px;color:var(--ink);line-height:1;white-space:nowrap}
  .hero-sub{left:46px;top:196px;font-size:14px;font-weight:600;color:var(--muted);white-space:nowrap}
  .learn-more{left:548px;top:186px;font-size:6.5px;font-weight:800;color:var(--orange);letter-spacing:.6px;padding-bottom:3px;border-bottom:1px solid var(--orange);width:62px;white-space:nowrap}
  .footer-rule{left:32px;right:0;height:1px;background:var(--line)}
  .footer-icon{width:8px;height:8px;border:1px solid var(--ink);background:var(--white)}
  .footer-text{font-size:5.5px;line-height:8px;color:var(--muted);white-space:nowrap}
  .kicker{font-family:"Lora",serif;font-size:15px;color:var(--orange);letter-spacing:.5px;white-space:nowrap}
  .lead{font-size:11px;font-weight:800;line-height:1.38;color:var(--ink)}
  .body-copy{font-size:6.4px;line-height:1.62;color:var(--muted)}
  .field{left:348px;width:270px;border:1px solid var(--line);font-size:6px;color:var(--muted);padding:6px 6px}
  .send{left:556px;width:62px;font-size:6.5px;font-weight:800;color:var(--orange);letter-spacing:.6px;padding-bottom:3px;border-bottom:1px solid var(--orange)}
</style>
</head>
<body>

<section class="page page--home">
  <div class="abs brand"><span class="brand-mark"></span>VELMAR</div>
  <nav class="abs nav"><span class="is-current">HOME</span><span>SERVICES</span><span>ABOUT</span><span>CONTACT</span></nav>
  <div class="abs nav-rule"></div>
  <div class="abs accent-bar" style="left:32px;top:164px;height:52px"></div>
  <h1 class="abs hero-title">VELMAR CONSULTING</h1>
  <p class="abs hero-sub">a specialized brand consultancy</p>
  <div class="abs learn-more">LEARN MORE</div>
  <div class="abs footer-icon" style="left:32px;top:338px"></div>
  <span class="abs footer-text" style="left:46px;top:338px">info@velmarconsulting.example</span>
  <div class="abs footer-icon" style="left:156px;top:338px"></div>
  <span class="abs footer-text" style="left:170px;top:338px">Lakemont, TX 75000</span>
  <span class="abs footer-text" style="left:560px;top:338px">© Velmar Consulting</span>
  <div class="abs footer-rule" style="top:350px"></div>
</section>

<section class="page page--services">
  <div class="abs brand"><span class="brand-mark"></span>VELMAR</div>
  <nav class="abs nav"><span>HOME</span><span class="is-current">SERVICES</span><span>ABOUT</span><span>CONTACT</span></nav>
  <div class="abs nav-rule"></div>
  <h2 class="abs kicker" style="left:46px;top:146px">WHAT WE DO</h2>
  <div class="abs accent-bar" style="left:60px;top:168px;height:48px"></div>
  <p class="abs lead" style="left:72px;top:166px;width:240px">We help our clients identify and develop protectable source identifiers through asset creation-oriented strategies.</p>
  <p class="abs body-copy" style="left:348px;top:118px;width:268px">Lorem ipsum dolor sit amet, consectetur adipiscing elit. Nullam id ex tellus. Donec rhoncus arcu id blandit sodales. Nam mattis purus, viverra eget feugiat in, scelerisque sit amet arcu. Suspendisse varius ullamcorper nulla non tincidunt neque dignissim quis. Donec euismod, quam eget gravida varius, dolor metus consequat elit, quis suscipit justo elit et ante. Morbi augue ex, interdum sed facilisis id, tincidunt pellentesque risus. Duis sapien magna, finibus quis varius volutpat, porttitor at magna nec parturient nunc nascetur ridiculus mus fusce non tellus eget ex bibendum molestie non ex quam. Donec rutrum congue neque a iaculis scelerisque enim vulputate ante vel, quis imperdiet sed blandit fusce tortor.</p>
  <div class="abs footer-icon" style="left:32px;top:328px"></div>
  <span class="abs footer-text" style="left:46px;top:328px">info@velmarconsulting.example</span>
  <div class="abs footer-icon" style="left:156px;top:328px"></div>
  <span class="abs footer-text" style="left:170px;top:328px">Lakemont, TX 75000</span>
  <span class="abs footer-text" style="left:560px;top:328px">© Velmar Consulting</span>
  <div class="abs footer-rule" style="top:340px"></div>
</section>

<section class="page page--contact">
  <div class="abs brand"><span class="brand-mark"></span>VELMAR</div>
  <nav class="abs nav"><span>HOME</span><span>SERVICES</span><span>ABOUT</span><span class="is-current">CONTACT</span></nav>
  <div class="abs nav-rule"></div>
  <h2 class="abs kicker" style="left:46px;top:136px">GET IN TOUCH</h2>
  <div class="abs accent-bar" style="left:60px;top:160px;height:92px"></div>
  <p class="abs lead" style="left:72px;top:158px;width:250px">We look forward to hearing from you.</p>
  <p class="abs body-copy" style="left:72px;top:176px;width:240px">We are highly selective about the clients we work with and the projects we work on. So, please provide us with your contact information and a few details about your business, and we will get back in touch with our availability and timeline for taking on new clients and projects.</p>
  <div class="abs field" style="top:116px;height:22px">Name</div>
  <div class="abs field" style="top:146px;height:22px">Email</div>
  <div class="abs field" style="top:176px;height:92px">Message</div>
  <div class="abs send" style="top:280px">SUBMIT</div>
  <div class="abs footer-icon" style="left:32px;top:334px"></div>
  <span class="abs footer-text" style="left:46px;top:334px">info@velmarconsulting.example</span>
  <div class="abs footer-icon" style="left:156px;top:334px"></div>
  <span class="abs footer-text" style="left:170px;top:334px">Lakemont, TX 75000</span>
  <span class="abs footer-text" style="left:560px;top:334px">© Velmar Consulting</span>
  <div class="abs footer-rule" style="top:346px"></div>
</section>

</body>
</html>
```